Management Consulting and Executive Coaching business needs a brochure.

I need a brochure that I can send to prospective clients. I provide management consulting services and executive coaching supports targeting organizations focused on social impact. I would like to see designs that use vibrant colors consistent with my logo (see attached) and that communicate forward motion/progress.

Target Market(s)

Social Impact leaders and organizations

Industry/Entity Type

Management Consulting

Font styles to use
Serif

Colors
b29ec9
85acd3
86cae7
87d0c7
acd037

Requirements
Must have
• Must have exciting, colorful, design features using words, art, imagery.
Should not have
• No dark or depressing imagery

```html
<!DOCTYPE html>
<html lang="en">
<head>
<meta charset="utf-8">
<title>Lumen Partnerships Flyer</title>
<link href="https://fonts.googleapis.com/css2?family=Montserrat:wght@400;500;600&family=Roboto+Slab:wght@700&display=swap" rel="stylesheet">
<style>
  :root {
    --purple: #5a0f73;
    --purple-deep: #3f0a55;
    --magenta: #8b1a8f;
    --pink: #e39bc7;
    --sky: #86cae7;
    --blue: #1f8fc1;
    --green: #5a9a2e;
    --ink: #555a60;
    --stage: #6bbcd9;
    --white: #ffffff;
  }
  * { box-sizing: border-box; margin: 0; padding: 0; }
  html, body { width: 1200px; height: 640px; overflow: hidden; }
  body {
    background: var(--stage);
    font-family: "Montserrat", Arial, sans-serif;
    position: relative;
  }
  .flyer {
    position: absolute;
    left: 387px; top: 20px;
    width: 425px; height: 600px;
    background: var(--purple);
    overflow: hidden;
    box-shadow: 0 8px 18px rgba(0,0,0,0.18);
  }
  .flyer-art { position: absolute; inset: 0; }
  .contact { position: absolute; right: 20px; text-align: right; color: var(--white); }
  .contact-phone { top: 280px; font-family: "Roboto Slab", Georgia, serif; font-size: 24px; font-weight: 700; letter-spacing: 0.5px; }
  .contact-web { top: 313px; font-size: 11.5px; font-weight: 500; }
  .section-title {
    position: absolute; left: 17px;
    color: var(--blue); font-size: 12.5px; font-weight: 600;
    border-bottom: 1px solid var(--magenta); line-height: 1.15;
  }
  .about-title { top: 330px; }
  .services-title { top: 469px; }
  .about-copy {
    position: absolute; left: 17px; top: 352px; width: 205px;
    color: var(--ink); font-size: 6.6px; line-height: 1.28; text-align: justify;
  }
  .about-copy p + p { margin-top: 6px; }
  .brand-badge {
    position: absolute; left: 250px; top: 363px;
    width: 106px; height: 106px; border-radius: 50%;
    background: var(--white); border: 2px solid var(--blue);
    display: flex; align-items: center; justify-content: center; text-align: center;
    color: var(--purple); font-size: 11px; font-weight: 500; line-height: 1.2; letter-spacing: 1px;
    text-transform: uppercase;
  }
  .service-label { position: absolute; left: 17px; color: var(--purple); font-size: 7.6px; font-weight: 600; }
  .service-item {
    position: absolute; color: var(--ink); font-size: 6.5px; line-height: 1.25;
    padding-left: 9px;
  }
  .service-item::before {
    content: ""; position: absolute; left: 0; top: 1.5px;
    width: 5px; height: 5px; border-radius: 50%; border: 1.2px solid var(--blue);
  }
  .service-note { display: block; font-size: 5px; margin-top: 2px; padding-left: 2px; }
  .col-a { left: 125px; }
  .col-b { left: 275px; }
</style>
</head>
<body>
  <article class="flyer">
    <svg class="flyer-art" viewBox="0 0 425 600" width="425" height="600" aria-hidden="false">
      <defs>
        <linearGradient id="photoTone" x1="0" y1="0" x2="1" y2="1">
          <stop offset="0" stop-color="#d9dcda"/>
          <stop offset="0.5" stop-color="#b7b2aa"/>
          <stop offset="1" stop-color="#8c8a88"/>
        </linearGradient>
      </defs>
      <rect width="425" height="600" fill="var(--purple)"/>
      <path d="M90,0 C55,80 55,190 75,262 C150,262 200,250 255,246 C320,240 380,228 425,218 V0 Z" fill="var(--magenta)" opacity="0.55"/>
      <path role="img" aria-label="Photo: a team of colleagues in discussion in a bright office lounge" d="M105,0 H425 V222 C360,232 300,240 240,252 C190,262 150,275 112,268 C85,200 80,100 105,0 Z" fill="url(#photoTone)"/>
      <path d="M60,275 C140,276 210,255 290,240 C350,229 400,222 425,220" fill="none" stroke="var(--pink)" stroke-width="5"/>
      <path d="M40,40 C50,120 60,220 120,280" fill="none" stroke="var(--sky)" stroke-width="1"/>
      <path d="M0,315 C120,296 250,330 330,398 C385,448 408,525 419,600 H0 Z" fill="var(--sky)"/>
      <path d="M0,306 C120,290 245,318 320,390 C372,440 396,520 406,600 H0 Z" fill="var(--white)"/>
      <rect x="0" y="596" width="425" height="4" fill="var(--green)"/>
    </svg>

    <div class="contact contact-phone">(415) 555-0142</div>
    <div class="contact contact-web">www.lumenpartnerships.com</div>

    <h2 class="section-title about-title">ABOUT US</h2>
    <div class="about-copy">
      <p>Lumen Partnerships LLC was formed based on the belief that promoting diverse perspectives leads to better solutions. The colors of the rainbow represent the beauty that is created by of diverse colors. Independently, the colors are lovely, and together the colors present a spectacular and beautiful palate. We promote diversity of thought, action, and inclusion.</p>
      <p>We believe that high performing leaders create and lead high performing organizations. We seek to partner with leaders and organizations across sectors who share a vision and mission to make a positive impact in the community.</p>
    </div>

    <div class="brand-badge">Lumen<br>Partnerships</div>

    <h2 class="section-title services-title">SERVICES</h2>
    <div class="service-label" style="top:496px">Executive Coaching:</div>
    <div class="service-label" style="top:550px">Management Consulting</div>

    <div class="service-item col-a" style="top:494px">Coaching to achieve personal<br>and professional goals</div>
    <div class="service-item col-a" style="top:522px">Strategic planning.</div>
    <div class="service-item col-a" style="top:537px">Board/executive team development.</div>
    <div class="service-item col-a" style="top:551px">Diversity training.</div>
    <div class="service-item col-a" style="top:566px">Program development and sustainability.</div>
    <div class="service-item col-a" style="top:580px">Management &amp; leadership training.</div>

    <div class="service-item col-b" style="top:498px">Group Coaching</div>
    <div class="service-item col-b" style="top:522px">Moderating/MC/Keynote<br>Speaker<span class="service-note">- (topics - leadership, mission-driven<br>philanthropy, social justice, motivational)</span></div>
    <div class="service-item col-b" style="top:564px">Facilitation - retreats, team planning,<br>analysis &amp; problem solving.</div>
  </article>
</body>
</html>
```